A-Stand Directional Sign Design

Objective:
We need a professional graphic design for an A-Stand sign that will guide customers arriving in our parking lot to our office. The design should be visually clear, welcoming, and aligned with our brand identity.
REQUIREMENTS:
Two versions of the design:
- One with an arrow pointing left
- One with an arrow pointing right
(This allows us to place the A-Stand anywhere and flip the graphic as needed.)
DIMENSIONS:
- Viewable Area: 30" x 40"
BRAND ALIGNMENT:
- Colors, fonts, and overall style should match our website: www.skornabel.com
- Clean, modern, and professional look consistent with our aviation/tourism brand
CONTENT:
- Clear directional arrow (left or right depending on version)
- Text: “Office Entrance” or similar concise wording (designers may propose alternatives if they improve clarity)
READABILITY:
- Bold, high-contrast design for visibility from a distance
- Simple layout that avoids clutter
DELIVERABLES:
- Final artwork in print-ready format (PDF preferred)
- Two versions: Arrow Left and Arrow Right
DESIGN GOAL:
Ensure customers can easily find our office upon arrival, while reinforcing skorNABEL’s professional and welcoming brand image.
Target Market(s)
Tourism

```html
<!DOCTYPE html>
<html lang="en">
<head>
<meta charset="utf-8">
<title>skorNABEL – Office Entrance A-Stand Signs</title>
<link rel="stylesheet" href="https://fonts.googleapis.com/css2?family=Montserrat:wght@600;800&display=swap">
<style>
  :root {
    --brand-blue: #0563ea;
    --band-white: #f4f4f4;
    --text-white: #ffffff;
    --page-bg: #ffffff;
  }
  * { box-sizing: border-box; margin: 0; padding: 0; }
  html, body {
    width: 1200px;
    height: 797px;
    overflow: hidden;
    background: var(--page-bg);
  }
  .sign-set {
    position: relative;
    width: 1200px;
    height: 797px;
    display: flex;
    justify-content: space-around;
    align-items: center;
    padding: 0 50px;
  }
  .sign-panel {
    width: 510px;
    height: 680px;
    display: flex;
    flex-direction: column;
    background: var(--brand-blue);
    box-shadow: 0 0 0 1px rgba(0,0,0,0.08);
  }
  .brand-band {
    height: 185px;
    display: flex;
    align-items: center;
    justify-content: center;
    gap: 12px;
  }
  .brand-mark {
    width: 22px;
    height: 22px;
    border-radius: 50%;
    background: var(--text-white);
  }
  .brand-name {
    font-family: "Montserrat", sans-serif;
    font-weight: 600;
    font-size: 30px;
    letter-spacing: 1px;
    color: var(--text-white);
  }
  .arrow-band {
    height: 170px;
    background: var(--band-white);
    display: flex;
    align-items: center;
    justify-content: center;
  }
  .direction-arrow {
    width: 340px;
    height: 150px;
    fill: var(--brand-blue);
  }
  .direction-arrow.is-right { transform: scaleX(-1); }
  .message-band {
    flex: 1;
    display: flex;
    align-items: center;
    justify-content: center;
    padding-bottom: 20px;
  }
  .message-text {
    font-family: "Montserrat", sans-serif;
    font-weight: 800;
    font-size: 64px;
    line-height: 1.08;
    text-align: center;
    color: var(--text-white);
    text-transform: uppercase;
  }
</style>
</head>
<body>
  <main class="sign-set">
    <section class="sign-panel sign-left" aria-label="Office entrance sign, arrow left">
      <header class="brand-band">
        <span class="brand-mark"></span>
        <span class="brand-name">skorNABEL</span>
      </header>
      <div class="arrow-band">
        <svg class="direction-arrow is-left" viewBox="0 0 340 150" aria-hidden="true">
          <path d="M10 75 L110 8 Q122 2 124 16 L118 48 L318 42 Q332 42 332 58 L332 92 Q332 108 318 108 L118 102 L124 134 Q122 148 110 142 Z"/>
        </svg>
      </div>
      <div class="message-band">
        <p class="message-text">Office<br>Entrance</p>
      </div>
    </section>

    <section class="sign-panel sign-right" aria-label="Office entrance sign, arrow right">
      <header class="brand-band">
        <span class="brand-mark"></span>
        <span class="brand-name">skorNABEL</span>
      </header>
      <div class="arrow-band">
        <svg class="direction-arrow is-right" viewBox="0 0 340 150" aria-hidden="true">
          <path d="M10 75 L110 8 Q122 2 124 16 L118 48 L318 42 Q332 42 332 58 L332 92 Q332 108 318 108 L118 102 L124 134 Q122 148 110 142 Z"/>
        </svg>
      </div>
      <div class="message-band">
        <p class="message-text">Office<br>Entrance</p>
      </div>
    </section>
  </main>
</body>
</html>
```